I need the following on my business card:
- Name: Dana Whitcomb
- License # 0M93216
- Title: Producer
- Phone: (555) 017-3904
- Email: Dana@CorbelInsuranceServices.com

- Company: Corbel Insurance Services
- Address: 27408 Larkmoor Ave Suite 610, Maple Ridge, OR 90217
- Website: www.CorbelInsuranceServices.com

Also add our slogan on the card: "Where Trust Meets Coverage"

```html
<!DOCTYPE html>
<html lang="en">
<head>
<meta charset="utf-8">
<title>Corbel Insurance Services – Business Card</title>
<link href="https://fonts.googleapis.com/css2?family=Poppins:wght@400;500;600;700&display=swap" rel="stylesheet">
<style>
  :root {
    --navy: #263079;
    --green: #1f9a3e;
    --paper: #ffffff;
    --backdrop: #eef1ee;
  }
  * { margin: 0; padding: 0; box-sizing: border-box; }
  html, body { width: 1200px; height: 1200px; overflow: hidden; }
  body {
    background: var(--backdrop);
    font-family: "Poppins", sans-serif;
    color: var(--navy);
    position: relative;
  }
  .card {
    position: absolute;
    left: 225px;
    width: 750px;
    height: 450px;
    background: var(--paper);
    overflow: hidden;
  }
  .card--front { top: 120px; }
  .card--back { top: 630px; display: flex; align-items: center; justify-content: center; }

  .identity { position: absolute; left: 70px; top: 50px; }
  .identity__name { font-size: 34px; font-weight: 600; line-height: 1.1; letter-spacing: -0.3px; }
  .identity__title { font-size: 19px; font-weight: 500; color: var(--green); letter-spacing: 4px; line-height: 1.3; }
  .identity__license { font-size: 16px; font-weight: 500; line-height: 1.4; }

  .brand-name {
    font-weight: 600;
    color: var(--navy);
    text-align: center;
    line-height: 1.15;
  }
  .card--front .brand-name {
    position: absolute; right: 60px; top: 62px;
    font-size: 21px; width: 200px;
  }
  .card--back .brand-name { font-size: 44px; width: 420px; }

  .slogan {
    position: absolute; left: 0; right: 0; top: 170px;
    text-align: center; font-size: 32px; font-weight: 600;
  }
  .slogan-rule {
    position: absolute; left: 97px; width: 556px; top: 218px;
    height: 2px; background: var(--green);
  }

  .contact { position: absolute; left: 72px; top: 250px; list-style: none; }
  .contact__item { display: flex; align-items: center; height: 33px; font-size: 23px; font-weight: 500; }
  .contact__item svg { width: 22px; height: 22px; margin-right: 12px; flex: none; }

  .address-band {
    position: absolute; left: 0; right: 0; bottom: 0; height: 84px;
    background: var(--navy); color: var(--paper); text-align: center;
    display: flex; flex-direction: column; justify-content: center;
  }
  .address-band__company { font-size: 21px; font-weight: 700; line-height: 1.3; }
  .address-band__street { font-size: 25px; font-weight: 400; line-height: 1.35; }
</style>
</head>
<body>
  <section class="card card--front">
    <div class="identity">
      <h1 class="identity__name">Dana Whitcomb</h1>
      <p class="identity__title">PRODUCER</p>
      <p class="identity__license">License # 0M93216</p>
    </div>
    <p class="brand-name">Corbel Insurance Services</p>

    <h2 class="slogan">Where Trust Meets Coverage</h2>
    <div class="slogan-rule"></div>

    <ul class="contact">
      <li class="contact__item">
        <svg viewBox="0 0 24 24" aria-hidden="true"><circle cx="12" cy="12" r="11" fill="#1f9a3e"/><path d="M8.2 6.5l1.8-.3 1.2 2.8-1.2 1a7 7 0 0 0 3.9 3.9l1-1.2 2.8 1.2-.3 1.8c-.2.8-1 1.3-1.8 1.2A9.5 9.5 0 0 1 7 8.3c-.1-.8.4-1.6 1.2-1.8z" fill="#fff"/></svg>
        phone : (555) 017-3904
      </li>
      <li class="contact__item">
        <svg viewBox="0 0 24 24" aria-hidden="true"><rect x="1" y="4" width="22" height="16" fill="#1f9a3e"/><path d="M1 4l11 9 11-9M1 20l8-7M23 20l-8-7" stroke="#fff" stroke-width="1.8" fill="none"/></svg>
        email : Dana@CorbelInsuranceServices.com
      </li>
      <li class="contact__item">
        <svg viewBox="0 0 24 24" aria-hidden="true" fill="none" stroke="#1f9a3e" stroke-width="1.8"><circle cx="12" cy="12" r="10"/><ellipse cx="12" cy="12" rx="4.5" ry="10"/><path d="M2 12h20M4 7h16M4 17h16"/></svg>
        website : www.CorbelInsuranceServices.com
      </li>
    </ul>

    <footer class="address-band">
      <p class="address-band__company">Corbel Insurance Services</p>
      <p class="address-band__street">27408 Larkmoor Ave Suite 610, Maple Ridge, OR 90217</p>
    </footer>
  </section>

  <section class="card card--back">
    <p class="brand-name">Corbel Insurance Services</p>
  </section>
</body>
</html>
```